Business Card for Lawyer

I'm looking for a business card for my new law firm, based in Ontario, Canada. I would prefer single sided. I am partial (but not limited) to white and blue color wise and like things understated. Also, if you can work in the red KT rating symbol from Penrowe-Calloway, that would be a plus.

Target Market(s)

Old people - so it should be easy to read.

Industry/Entity Type

Business

Contact Information for Business Card

See the specs in the word document below. Also, see the design for my website. The card should have a similar look to the site.

Requirements
Must have
• Everything listed in the business card specs. I don't mind having the address set off at the bottom of the card on its own line.
Should not have
• 1) Any sort of design that could also be used by a tattoo parlour or a tarot card reader, mystic etc.
• 2) There should not be any photographs of me (or anyone else).

```html
<!DOCTYPE html>
<html lang="en">
<head>
<meta charset="utf-8">
<title>Whitmore Law Firm – Business Card</title>
<link rel="stylesheet" href="https://fonts.googleapis.com/css2?family=Libre+Baskerville&family=Open+Sans:wght@400;600&family=Libre+Franklin:wght@600&display=swap">
<style>
  :root {
    --backdrop: #6f665d;
    --card-dark: #1c1c1c;
    --card-darker: #101010;
    --cream: #f8f5ee;
    --white: #ffffff;
    --divider: #bdbdbd;
    --accent-blue: #3aa0e0;
    --bullet-blue: #3f5fb0;
    --brand-red: #c9432a;
    --brand-purple: #5b3a8c;
    --badge-grey: #9a9a9a;
    --badge-panel: #d8d8d8;
    --ink: #1a1a1a;
  }
  * { margin: 0; padding: 0; box-sizing: border-box; }
  html, body { width: 1200px; height: 1200px; overflow: hidden; }
  body { background: var(--backdrop); position: relative; font-family: "Open Sans", sans-serif; }

  .card {
    position: absolute; left: 109px; width: 971px; height: 567px;
    background: linear-gradient(160deg, var(--card-dark), var(--card-darker));
    box-shadow: 0 6px 18px rgba(0,0,0,.45);
    overflow: hidden;
  }
  .card--front { top: 18px; }
  .card--back { top: 612px; height: 566px; }

  .corner-tab { position: absolute; left: 0; top: 0; }

  .holder-name {
    position: absolute; left: 44px; top: 82px;
    font-family: "Libre Baskerville", serif; font-weight: 400; font-size: 30px; color: var(--white);
    white-space: nowrap;
  }
  .holder-degree {
    position: absolute; left: 44px; top: 124px;
    font-size: 21px; color: var(--accent-blue); letter-spacing: .5px;
  }

  .brand__dot { position: absolute; border-radius: 50%; background: var(--brand-red); }
  .brand__divider { position: absolute; width: 2px; background: var(--divider); }
  .brand__name {
    position: absolute; white-space: nowrap;
    font-family: "Libre Baskerville", serif; font-weight: 400; color: var(--white); letter-spacing: 1px;
  }
  .card--front .brand__dot { left: 437px; top: 40px; width: 148px; height: 148px; }
  .card--front .brand__divider { left: 608px; top: 50px; height: 104px; }
  .card--front .brand__name { left: 625px; top: 64px; font-size: 40px; line-height: 46px; }
  .card--back .brand__dot { left: 105px; top: 164px; width: 216px; height: 216px; }
  .card--back .brand__divider { left: 346px; top: 215px; height: 118px; }
  .card--back .brand__name { left: 371px; top: 210px; font-size: 66px; line-height: 80px; }

  .contact { position: absolute; left: 44px; list-style: none; }
  .contact li { display: flex; align-items: center; gap: 14px; height: 30px; color: var(--white); font-size: 21px; white-space: nowrap; }
  .contact svg { width: 24px; height: 24px; flex: none; }
  .contact--address { top: 242px; }
  .contact--phones { top: 286px; }
  .contact--online { top: 361px; }

  .practice-band { position: absolute; left: 0; bottom: 0; }
  .practice-list {
    position: absolute; left: 0; top: 0; list-style: none;
    font-family: "Libre Franklin", sans-serif; font-weight: 600; font-size: 21px; color: var(--ink);
  }
  .practice-list li { position: absolute; white-space: nowrap; display: flex; align-items: center; gap: 5px; line-height: 28px; }
  .practice-list li::before { content: ""; width: 14px; height: 14px; border-radius: 50%; background: var(--bullet-blue); }

  .rating-badge__circle { position: absolute; left: 671px; top: 467px; width: 72px; height: 72px; border-radius: 50%; background: var(--badge-grey); }
  .rating-badge__panel { position: absolute; left: 753px; top: 464px; width: 190px; height: 84px; border-radius: 4px; background: var(--badge-panel); }

  .tagline-band {
    position: absolute; left: 0; right: 0; top: 494px; height: 51px;
    background: var(--brand-purple); color: var(--white);
    display: flex; align-items: center; justify-content: center;
    font-size: 23px; letter-spacing: 1.5px; white-space: nowrap;
  }
</style>
</head>
<body>

<section class="card card--front">
  <svg class="corner-tab" width="200" height="26" viewBox="0 0 200 26"><path d="M0 0H200L176 26H0Z" fill="var(--cream)"/></svg>

  <h1 class="holder-name">Daniel R. Whitmore</h1>
  <p class="holder-degree">B.A. &amp; J.D.</p>

  <span class="brand__dot"></span>
  <span class="brand__divider"></span>
  <p class="brand__name">WHITMORE<br>LAW FIRM</p>

  <ul class="contact contact--address">
    <li><svg viewBox="0 0 24 24"><rect width="24" height="24" fill="var(--white)"/><path d="M4 13L12 5L20 13H17V20H7V13Z" fill="var(--ink)"/></svg>48 Carden Lane East, Ground Floor, Hamilton, ON L8N 2T4</li>
  </ul>
  <ul class="contact contact--phones">
    <li><svg viewBox="0 0 24 24"><rect width="24" height="24" fill="var(--white)"/><path d="M4 9Q12 3 20 9L17 11L15 9H9L7 11Z M7 13H17L18 19H6Z" fill="var(--ink)"/></svg>647-555-0182</li>
    <li><svg viewBox="0 0 24 24"><rect width="24" height="24" fill="var(--white)"/><path d="M4 9Q12 3 20 9L17 11L15 9H9L7 11Z M6 13H18V19H6Z" fill="var(--ink)"/><rect x="9" y="15" width="6" height="2" fill="var(--white)"/></svg>647.555.0147</li>
  </ul>
  <ul class="contact contact--online">
    <li><svg viewBox="0 0 24 24"><rect width="24" height="24" fill="var(--white)"/><circle cx="12" cy="12" r="7" fill="none" stroke="var(--ink)" stroke-width="1.8"/><path d="M5 12H19M12 5Q8 12 12 19M12 5Q16 12 12 19" fill="none" stroke="var(--ink)" stroke-width="1.5"/></svg>www.whitmorefirm.ca</li>
    <li><svg viewBox="0 0 24 24"><rect x="2" y="5" width="20" height="14" fill="none" stroke="var(--white)" stroke-width="2"/><path d="M2 5L12 13L22 5M2 19L9 11M22 19L15 11" fill="none" stroke="var(--white)" stroke-width="1.5"/></svg>email@whitmorefirm.ca</li>
  </ul>

  <svg class="practice-band" width="971" height="139" viewBox="0 0 971 139"><path d="M0 20H772L800 0H971V139H0Z" fill="var(--cream)"/></svg>
  <ul class="practice-list">
    <li style="left:36px;top:476px">Barrister</li>
    <li style="left:173px;top:476px">Solicitor &amp; Notary Public</li>
    <li style="left:483px;top:476px">Trial Lawyer</li>
    <li style="left:173px;top:514px">Lawyer</li>
    <li style="left:298px;top:514px">Litigation Counsel</li>
  </ul>
  <span class="rating-badge__circle"></span>
  <span class="rating-badge__panel"></span>
</section>

<section class="card card--back">
  <span class="brand__dot"></span>
  <span class="brand__divider"></span>
  <p class="brand__name">WHITMORE<br>LAW FIRM</p>
  <p class="tagline-band">DELIVERING THE OUTCOMES YOU NEED</p>
</section>

</body>
</html>
```